To design a new professional and elegant website design

To design an elegant and professional business website - e.g. Responsive WordPress theme.

Please refer to the existing site www.verlow-partners.com for information regarding the business service and the content that will be included.

While the designer can suggest colors, the current logo (see attached) should remain.
Although I have indicated Sans Serif as a font, I welcome alternative suggestions.
Updates

To all designers:

I have attached additional .psd files of the logo for your use in the design of the new site (theme). As posted in an earlier response, I wish to keep the logo and the color blue. You are welcome to either work with or change the green.

- Please avoid making the page too busy.

- Avoid stock business pictures such as the people working on a document with the calculator the generic people in suits. Ideally, I would like unique media.

- Do not include contact information on the home page. There are two offices – 1 in Houston and one in UK and I want to make sure that we distinguish between the two.

- Use bullets rather than check boxes .

- Do not use the social links as we do not currently use them - this may change in the future

- The footer should include: sitemap, Terms of Use, Privacy Policy and the 2014 Copyright notice. The other pages should be accessible via a menu

Hope this helps.
Thanks

To all participants,

I have increased the budget by an additional £200.

Regards,

Target Market(s)

As you may glean from the website, the company is a management consultancy serving Meridale 400 companies and private equity firms. Companies include: Tolk, GX, KF, Navine Rosset Companies, Selo Varna...

Sites that may influence the design include:

http://www.hvn.co.uk/consulting/
http://www.qz.com/UK/en/Services/Advisory
http://www.kolt.com/industry-expertise/technology/index.aspx
http://www.obvaleprojects.com/news

Industry/Entity Type

Business Service

Font styles to use
Sans Serif

Colors

Designer to choose colors to be used in the design.

Requirements
Must have
• Existing blue logo - globe with the V & P (see attached). The green is not necessary
Must function of a WordPress responsive platform.
Nice to have
• While the new theme will need to be consistent throughout the site, the home page can vary from the child pages.
Should not have
• Common stock images. If used, the images and icons should be unique.

```html
<!DOCTYPE html>
<html lang="en">
<head>
<meta charset="utf-8">
<title>Verlow Partners</title>
<link rel="stylesheet" href="https://fonts.googleapis.com/css2?family=Oswald:wght@300;400&family=Open+Sans:ital,wght@0,400;0,700;1,400&display=swap">
<style>
:root{
  --navy:#16233a;
  --navy-deep:#0e1628;
  --panel-solid:#333f56;
  --panel-glass:rgba(26,36,58,.72);
  --brand-blue:#1d8ad6;
  --text-dark:#1d1d1d;
  --text-mid:#666;
  --panel-text:#8e9bb2;
  --footer-link:#8ea0bf;
  --white:#fff;
}
*{margin:0;padding:0;box-sizing:border-box}
html,body{width:1074px;height:1200px;overflow:hidden;background:var(--white)}
body{position:relative;font-family:"Open Sans",Verdana,sans-serif;color:var(--text-dark)}
.site-header{position:absolute;left:0;top:0;width:1074px;height:138px;background:linear-gradient(90deg,#1a2840,#16233a 60%,#1b2942)}
.brand{position:absolute;left:34px;top:34px;display:flex;align-items:center;gap:10px}
.brand-dot{width:60px;height:60px;border-radius:50%;background:var(--brand-blue)}
.brand-name{font-family:"Oswald",sans-serif;font-weight:300;font-size:26px;line-height:30px;color:var(--white)}
.util-nav{position:absolute;right:34px;top:31px;font-size:10.5px;color:#8a9ab5}
.util-nav span{margin:0 8px}
.main-nav{position:absolute;right:34px;top:94px;display:flex;gap:43px;font-size:10.5px;color:var(--white);letter-spacing:.2px}
.hero{position:absolute;left:0;top:138px;width:1074px;height:533px}
.hero-photo{position:absolute;inset:0;background:linear-gradient(100deg,#2b4a6e 0%,#5f84a8 25%,#b9cde0 45%,#7e97b2 62%,#3c526d 80%,#2c3e56 100%)}
.feature{position:absolute;width:266px;text-align:center;color:var(--panel-text)}
.feature h2{font-family:"Oswald",sans-serif;font-weight:400;font-size:29px;color:var(--white);margin-bottom:20px}
.feature p{font-size:11px;line-height:20px;padding:0 10px;margin-bottom:24px}
.feature svg{display:block;margin:0 auto}
.f-top{left:775px;top:0;height:267px;background:var(--panel-glass);padding-top:56px;border-bottom:1px dashed rgba(255,255,255,.6)}
.f-left{left:509px;top:267px;height:266px;background:var(--panel-solid);padding-top:56px;border-right:1px dashed rgba(255,255,255,.6)}
.f-right{left:775px;top:267px;height:266px;background:var(--panel-glass);padding-top:56px}
.section-title{font-family:"Oswald",sans-serif;font-weight:400;font-size:29px;line-height:34px;color:var(--text-dark)}
.section-sub{font-family:"Oswald",sans-serif;font-weight:300;font-size:13px;color:var(--text-mid);margin-top:4px;white-space:nowrap}
.col{position:absolute;top:702px}
.intro{left:33px;width:487px}
.intro-photo{margin-top:34px;width:487px;height:167px;background:linear-gradient(120deg,#dfe4ea 0%,#9aa6b4 35%,#3b4657 70%,#232b38 100%)}
.intro p{margin-top:27px;font-size:11px;line-height:20px}
.intro strong{font-weight:700}
.news{left:553px;width:225px}
.news-list{list-style:none;margin-top:28px}
.news-list li{padding:4px 0 8px;border-bottom:1px dotted #aaa;margin-bottom:8px}
.news-list li:last-child{border:none}
.news-date{font-size:10.5px;line-height:18px}
.news-title{font-size:10.5px;line-height:17px;font-weight:700}
.testimonials{left:813px;width:230px}
.quote-head{margin-top:36px;font-size:10.5px;font-weight:700;line-height:17px}
.quote{margin-top:18px;font-size:10.5px;font-style:italic;line-height:20px;color:#333}
.author{margin-top:8px;font-size:10.5px;line-height:17px}
.author b{font-weight:700}
.dots{display:flex;gap:4px;margin:64px 0 0 82px}
.dots i{width:10px;height:10px;border-radius:50%;background:#d3d7dc}
.dots i.on{background:var(--navy-deep)}
.site-footer{position:absolute;left:34px;top:1098px;width:1006px;height:67px;background:var(--navy-deep);border-radius:3px;display:flex;justify-content:space-between;align-items:center;padding:0 22px;font-size:10.5px;color:var(--footer-link)}
.site-footer b{color:var(--white)}
</style>
</head>
<body>
<header class="site-header">
  <div class="brand"><div class="brand-dot"></div><div class="brand-name">Verlow<br>Partners</div></div>
  <div class="util-nav">Join Us<span>|</span>Career<span>|</span>Help</div>
  <nav class="main-nav"><span>ABOUT VERLOW</span><span>VALUES</span><span>SERVICES</span><span>CLIENTS</span><span>CONTACT</span></nav>
</header>

<section class="hero">
  <div class="hero-photo" role="img" aria-label="Glass office towers seen from below against a pale blue sky"></div>
  <div class="feature f-top">
    <h2>Lorem ipsum</h2>
    <p>Sed ut perspiciatis unde omnis iste natus error sit voluptatem accusantium doloremque laudantium</p>
    <svg width="34" height="34" viewBox="0 0 34 34"><circle cx="17" cy="17" r="17" fill="#fff"/><path d="M17 8v15M10 17l7 7 7-7" stroke="#1a2438" stroke-width="3.5" fill="none" stroke-linecap="round" stroke-linejoin="round"/></svg>
  </div>
  <div class="feature f-left">
    <h2>Lorem ipsum</h2>
    <p>Sed ut perspiciatis unde omnis iste natus error sit voluptatem accusantium doloremque laudantium</p>
    <svg width="34" height="34" viewBox="0 0 34 34"><circle cx="17" cy="17" r="17" fill="#fff"/><path d="M17 8v15M10 17l7 7 7-7" stroke="#1a2438" stroke-width="3.5" fill="none" stroke-linecap="round" stroke-linejoin="round"/></svg>
  </div>
  <div class="feature f-right">
    <h2>Lorem</h2>
    <p>Sed ut perspiciatis unde omnis iste natus error sit voluptatem accusantium doloremque laudantium</p>
    <svg width="34" height="34" viewBox="0 0 34 34"><circle cx="17" cy="17" r="17" fill="#fff"/><path d="M17 8v15M10 17l7 7 7-7" stroke="#1a2438" stroke-width="3.5" fill="none" stroke-linecap="round" stroke-linejoin="round"/></svg>
  </div>
</section>

<section class="col intro">
  <h2 class="section-title">Loprem ipsum</h2>
  <div class="section-sub">Lorem ipsum dolor sit amet, consectetur adipisicing elit, sed do eiusmod</div>
  <div class="intro-photo" role="img" aria-label="Business handshake beside a tablet on a desk"></div>
  <p>Sed ut perspiciatis unde omnis iste natus error sit voluptatem accusantium doloremque laudantium, totam rem aperiam, eaque ipsa quae ab illo inventore veritatis et quasi archi-tecto beatae vitae dicta sunt explicabo...<strong>Read More</strong></p>
</section>

<section class="col news">
  <h2 class="section-title">News</h2>
  <div class="section-sub">Lorem ipsum dolor sit amet</div>
  <ul class="news-list">
    <li><div class="news-date">02/06/2014</div><div class="news-title">Lorem ipsum dolor sit amet, consectetur adipisicing elit</div></li>
    <li><div class="news-date">01/12/2014</div><div class="news-title">Lorem ipsum dolor sit amet, consectetur adipisicing elit</div></li>
    <li><div class="news-date">12/28/2013</div><div class="news-title">Lorem ipsum dolor sit amet, consectetur adipisicing elit</div></li>
    <li><div class="news-date">11/18/2013</div><div class="news-title">Lorem ipsum dolor sit amet, consectetur adipisicing elit</div></li>
  </ul>
</section>

<section class="col testimonials">
  <h2 class="section-title">Testimonials</h2>
  <div class="section-sub">Lorem ipsum dolor sit amet, consectetur adipisicing</div>
  <div class="quote-head">Lorem ipsum dolor sit amet, consectetur adipisicing elit</div>
  <p class="quote">“ Sed ut perspiciatis unde omnis iste natus error sit voluptatem accusantium doloremque laudantium, totam rem aperiam, eaqueveritatis et quasi architecto beatae vitae dicta sunt explicabo. ”</p>
  <div class="author"><b>Aron Pelk</b><br>CEO, Company Name</div>
  <div class="dots"><i class="on"></i><i></i><i></i><i></i><i></i></div>
</section>

<footer class="site-footer">
  <div>Sitemap | Terms of Use | Privacy Policy</div>
  <div>All rights reserved, <b>Verlow Partners LLC</b>, 2005-2014</div>
</footer>
</body>
</html>
```